Business Card - Apex Wellness

Please use the logo / design elements and font to design a business card that is eye catching and informative. If using "Direct Primary Care" logo element, you don't have to spell it out in the text.

Dr. Brendan Halvik
Apex Wellness - Direct Primary Care
4817 Tillbrook Rd. Suite 305
Fort Smith, AR 72916
Phone: 479-555-0137
ApexWellnessAR.example

```html
<!DOCTYPE html>
<html lang="en">
<head>
<meta charset="utf-8">
<title>Apex Wellness – Business Card</title>
<link rel="stylesheet" href="https://fonts.googleapis.com/css2?family=Poppins:wght@300;400;500;600&family=Montserrat:wght@300;400&display=swap">
<style>
  :root {
    --backdrop: #1c1c1f;
    --navy: #0a1842;
    --navy-light: #1d2f66;
    --sky: #38b2e8;
    --white: #ffffff;
    --muted: #d7deee;
  }
  * { box-sizing: border-box; margin: 0; padding: 0; }
  html, body {
    width: 1200px; height: 900px; overflow: hidden;
    background: var(--backdrop);
  }
  .stage {
    width: 1200px; height: 900px;
    display: flex; align-items: center; justify-content: center; gap: 40px;
  }
  .card {
    position: relative;
    width: 540px; height: 310px;
    border-radius: 22px;
    overflow: hidden;
    background: var(--navy);
    box-shadow: 0 18px 40px rgba(0,0,0,.45);
    color: var(--white);
    font-family: "Poppins", sans-serif;
  }

  /* Front */
  .card-front {
    background: linear-gradient(135deg, var(--navy-light) 0%, var(--navy) 60%);
    display: flex; flex-direction: column; align-items: center; justify-content: center;
  }
  .brand-lockup { display: flex; align-items: center; gap: 16px; }
  .brand-dot {
    width: 38px; height: 38px; border-radius: 50%;
    background: var(--sky);
  }
  .brand-name {
    font-weight: 500; font-size: 50px; letter-spacing: -1px; color: var(--white);
  }
  .tagline {
    margin-top: 10px;
    display: flex; align-items: center; gap: 14px;
    font-size: 15px; font-weight: 500; letter-spacing: .5px; color: var(--white);
  }
  .tagline .rule { width: 70px; height: 1px; background: var(--muted); }

  /* Back */
  .back-brand {
    position: absolute; top: 34px; right: 36px;
    display: flex; flex-direction: column; align-items: flex-end;
  }
  .back-brand .brand-lockup { gap: 10px; }
  .back-brand .brand-dot { width: 22px; height: 22px; }
  .back-brand .brand-name { font-size: 30px; letter-spacing: -.5px; }
  .back-brand .tagline { margin-top: 4px; font-size: 10px; gap: 8px; }
  .back-brand .tagline .rule { width: 40px; }

  .person {
    position: absolute; left: 36px; top: 132px;
  }
  .person-name {
    font-weight: 600; font-size: 25px; color: var(--sky); letter-spacing: -.3px;
  }
  .person-role {
    font-weight: 300; font-size: 13px; color: var(--white); margin-top: 2px;
    font-family: "Montserrat", sans-serif;
  }
  .divider {
    position: absolute; left: 276px; top: 142px;
    width: 1px; height: 80px; background: var(--sky);
    transform: rotate(18deg);
  }
  .contacts {
    position: absolute; left: 300px; top: 150px;
    list-style: none;
    font-family: "Montserrat", sans-serif; font-weight: 300; font-size: 13px;
  }
  .contacts li { display: flex; align-items: center; gap: 8px; line-height: 22px; }
  .contacts svg { width: 12px; height: 12px; fill: var(--sky); flex: none; }

  .address-band {
    position: absolute; left: 0; right: 0; bottom: 0; height: 40px;
    background: var(--sky);
    display: flex; align-items: center; justify-content: space-between;
    padding: 0 24px 0 36px;
    font-family: "Montserrat", sans-serif; font-weight: 400; font-size: 13px; color: var(--white);
  }
  .address-band .band-dot {
    width: 20px; height: 20px; border-radius: 50%; background: var(--navy);
  }
</style>
</head>
<body>
<main class="stage">

  <section class="card card-front" aria-label="Business card front">
    <div class="brand-lockup">
      <span class="brand-dot"></span>
      <span class="brand-name">Apex Wellness</span>
    </div>
    <div class="tagline">
      <span class="rule"></span>
      <span>Direct Primary Care</span>
      <span class="rule"></span>
    </div>
  </section>

  <section class="card card-back" aria-label="Business card back">
    <div class="back-brand">
      <div class="brand-lockup">
        <span class="brand-dot"></span>
        <span class="brand-name">Apex Wellness</span>
      </div>
      <div class="tagline">
        <span class="rule"></span>
        <span>Direct Primary Care</span>
        <span class="rule"></span>
      </div>
    </div>

    <div class="person">
      <p class="person-name">Dr. Brendan Halvik</p>
      <p class="person-role">Founder / Physician</p>
    </div>

    <span class="divider"></span>

    <ul class="contacts">
      <li>
        <svg viewBox="0 0 24 24" aria-hidden="true"><path d="M6.6 10.8a15.1 15.1 0 0 0 6.6 6.6l2.2-2.2a1 1 0 0 1 1-.25 11.4 11.4 0 0 0 3.6.57 1 1 0 0 1 1 1V20a1 1 0 0 1-1 1A17 17 0 0 1 3 4a1 1 0 0 1 1-1h3.5a1 1 0 0 1 1 1c0 1.25.2 2.45.57 3.57a1 1 0 0 1-.25 1z"/></svg>
        479-555-0137
      </li>
      <li>
        <svg viewBox="0 0 24 24" aria-hidden="true"><path d="M2 5h20v14H2zm2 2v.5l8 5 8-5V7zm0 3v7h16v-7l-8 5z"/></svg>
        info@apexwellnessar.example
      </li>
      <li>
        <svg viewBox="0 0 24 24" aria-hidden="true"><circle cx="12" cy="12" r="10"/></svg>
        ApexWellnessAR.example
      </li>
    </ul>

    <div class="address-band">
      <span>4817 Tillbrook Rd. Suite 305 Fort Smith, AR 72916</span>
      <span class="band-dot"></span>
    </div>
  </section>

</main>
</body>
</html>
```